Fresh & Clean *NEW* BUSINESS CARD Needed - OPTOMETRY Clinic/Optical

High-tech optometry practice with 3 doctors seeking new business card.  We provide eye exams, sell, designer glasses/contacts/specialty eyewear and treat ocular diseases.  For our business cards, we are seeking fresh, clean, and crisp design as we grow our team (staffing change).  Simply adding doctors is making the card look busy/cluttered.
 Looking for professional, less cluttered look yet still have our logo, doctor names, phone, address, and website....If possible!  :)
Names:
Marcia Trelford, O.D.
Ned Pallister, O.D.
Oona Ferrant, O.D.
Phone: 555-014-2738
Website: www.BrightLensHub.example
Address:  417 Garnet R. Holloway, Harbor Point, XY 00000
Ultimately we have the main business card with all doctor sames and that card has two versions  (front is always the same).  The back has two designs (1) displays next appointment time/date, (2) for "general use" (non-appointment.)    I have attached what we have used in the past.  
We also need a design template for each team member in our practice with their name, title, and email.   Those should be designed with the "general use" back (see attached).
**Open to entirely new design so don't feel obligated to keep current format.  Need new perspective!  Also including our watermark and some other design features we have consistently used in past in our portfolio.  Included are two options for logos--vertical and horizontal.
**I also would like to remove "Member of Sight Alliance" on our logo if possible**
 Other image files available upon request.

Target Market(s)

New patient & Current Patients

Industry/Entity Type

Optometry

Contact Information for Business Card

High-tech optometry practice with 3 doctors seeking new business card.  We provide eye exams, sell, designer glasses/contacts/specialty eyewear and treat ocular diseases.  For our business cards, we are seeking fresh, clean, and crisp design as we grow our team (staffing change).  Simply adding doctors is making the card look busy/cluttered.  Looking for professional, less cluttered look yet still have our logo, doctor names, phone, address, and website....If possible!  :) Names: Marcia Trelford, O.D. Ned Pallister, O.D. Oona Ferrant, O.D. Phone: 555-014-2738 Website: www.BrightLensHub.example Address:  417 Garnet R. Holloway, Harbor Point, XY 00000 Ultimately we have the main business card with all doctor sames and that card has two versions  (front is always the same).  The back has two designs (1) displays next appointment time/date, (2) for "general use" (non-appointment.)    I have attached what we have used in the past.   We also need a design template for each team member in our practice with their name, title, and email.   Those should be designed with the "general use" back (see attached). **Open to entirely new design so don't feel obligated to keep current format.  Need new perspective!  Also including our watermark and some other design features we have consistently used in past in our portfolio.  Included are two options for logos--vertical and horizontal. **I also would like to remove "Member of Sight Alliance" on our logo if possible**  Other image files available upon request.

Font styles to use
Other font styles liked:
• We have used Montserrat / Yellowtail in the past

Colors

Designer to choose colors to be used in the design.

Requirements
Must have
• Clean & Fresh Design with Logo / Info provided in description. Horizontal orientation. **I have included the CMYK colors we currently have in our logo.
Should not have
• Cluttered

```html
<!DOCTYPE html>
<html lang="en">
<head>
<meta charset="utf-8">
<title>BrightLens Hub – Business Card</title>
<link rel="stylesheet" href="https://fonts.googleapis.com/css2?family=Montserrat:wght@400;500;700&display=swap">
<style>
  :root {
    --backdrop: #707070;
    --card: #ffffff;
    --ink-grey: #6d6e71;
    --gold: #d9ab16;
    --sky: #a8dde8;
    --slate: #557080;
  }
  * { box-sizing: border-box; margin: 0; padding: 0; }
  html, body {
    width: 1200px; height: 1015px; overflow: hidden;
    background: var(--backdrop);
    font-family: "Montserrat", sans-serif;
  }
  .stage { position: relative; width: 1200px; height: 1015px; }
  .card {
    position: absolute; width: 620px; height: 354px;
    background: var(--card); overflow: hidden;
    box-shadow: 0 6px 14px rgba(0,0,0,.35);
  }
  .card-front { left: 200px; top: 105px; }
  .card-back { left: 380px; top: 545px; }

  /* front */
  .brand {
    position: absolute; left: 0; right: 0; top: 120px;
    display: flex; align-items: center; justify-content: center; gap: 16px;
  }
  .brand-dot { width: 46px; height: 46px; border-radius: 50%; background: var(--sky); }
  .brand-name { font-size: 44px; font-weight: 500; color: var(--ink-grey); letter-spacing: .5px; }
  .front-web {
    position: absolute; left: 40px; right: 40px; bottom: 58px;
    display: flex; align-items: center; gap: 14px;
    font-size: 15px; letter-spacing: 1.5px; color: var(--ink-grey);
    white-space: nowrap;
  }
  .front-web .rule { flex: 1; height: 1px; background: var(--gold); }
  .front-web .accent { color: var(--gold); }

  /* back */
  .back-circle {
    position: absolute; right: -150px; top: -190px;
    width: 400px; height: 400px; border-radius: 50%; background: var(--sky);
  }
  .back-info { position: absolute; left: 50px; top: 96px; color: var(--ink-grey); }
  .doctors { list-style: none; font-size: 19px; font-weight: 700; line-height: 1.3; }
  .doctors .title { color: var(--gold); font-weight: 500; }
  .divider { width: 150px; height: 1px; background: var(--ink-grey); opacity: .6; margin: 12px 0; }
  .address { font-size: 14px; line-height: 1.35; }
  .contact { list-style: none; font-size: 14px; line-height: 1.6; }
  .contact li { display: flex; align-items: center; gap: 8px; white-space: nowrap; }
  .contact svg { width: 16px; height: 16px; flex: none; }
</style>
</head>
<body>
<main class="stage">
  <section class="card card-front" aria-label="Card front">
    <div class="brand">
      <span class="brand-dot"></span>
      <span class="brand-name">BrightLens Hub</span>
    </div>
    <div class="front-web">
      <span class="rule"></span>
      <span>www.<span class="accent">BrightLensHub</span>.example</span>
      <span class="rule"></span>
    </div>
  </section>

  <section class="card card-back" aria-label="Card back">
    <div class="back-circle"></div>
    <div class="back-info">
      <ul class="doctors">
        <li>Marcia Trelford, <span class="title">O.D.</span></li>
        <li>Ned Pallister, <span class="title">O.D.</span></li>
        <li>Oona Ferrant, <span class="title">O.D.</span></li>
      </ul>
      <div class="divider"></div>
      <p class="address">417 Garnet R. Holloway, Harbor<br>Point, XY 00000</p>
      <div class="divider"></div>
      <ul class="contact">
        <li>
          <svg viewBox="0 0 16 16" aria-hidden="true"><circle cx="8" cy="8" r="8" fill="#d9ab16"/><path d="M5.3 4.5l1.3-.3.8 1.8-.9.7a5 5 0 0 0 2.4 2.4l.7-.9 1.8.8-.3 1.3c-3.4.3-6.1-2.4-5.8-5.8z" fill="#fff"/></svg>
          555-014-2738
        </li>
        <li>
          <svg viewBox="0 0 16 16" aria-hidden="true"><circle cx="8" cy="8" r="8" fill="#d9ab16"/><g fill="none" stroke="#fff" stroke-width=".9"><circle cx="8" cy="8" r="4"/><ellipse cx="8" cy="8" rx="1.8" ry="4"/><path d="M4 8h8"/></g></svg>
          www.BrightLensHub.example
        </li>
      </ul>
    </div>
  </section>
</main>
</body>
</html>
```